Need a corporate background Image with our existing logo for Zoom or Microsoft Teams

Hi,

We require a corporate background image with our existing logo use with Zoom or Microsoft Teams.

Our existing logo is at https://www.halvenrock-systems.com/images/logo_top.png

Thank you.

```html
<!DOCTYPE html>
<html lang="en">
<head>
<meta charset="utf-8">
<title>Halvenrock Systems – Video Call Backgrounds</title>
<link rel="stylesheet" href="https://fonts.googleapis.com/css2?family=Arimo:wght@700&display=swap">
<style>
  :root {
    --page: #ffffff;
    --navy-deep: #101c4c;
    --navy: #13266b;
    --royal: #17399a;
    --brand-blue: #3d8ef0;
    --glow-cyan: #1fc3e6;
    --glow-dark: #0d1a45;
    --hex-faint: #1a3c8c;
    --shirt-light: #bcdcf5;
    --shirt-mid: #8fbde6;
  }
  * { box-sizing: border-box; margin: 0; padding: 0; }
  html, body {
    width: 1004px;
    height: 1200px;
    overflow: hidden;
    background: var(--page);
  }
  .sheet {
    position: relative;
    width: 1004px;
    height: 1200px;
  }
  .backdrop {
    position: absolute;
    left: 69px;
    width: 867px;
    height: 485px;
    overflow: hidden;
    background: linear-gradient(100deg, var(--royal) 0%, var(--navy) 40%, var(--navy-deep) 100%);
  }
  .backdrop--with-host { top: 73px; }
  .backdrop--plain { top: 631px; }

  .glow-hex-field {
    position: absolute;
    left: 448px;
    top: 0;
    width: 419px;
    height: 436px;
    background:
      radial-gradient(ellipse at 85% 30%, rgba(31,195,230,0.45) 0%, rgba(31,195,230,0.18) 45%, rgba(31,195,230,0) 75%),
      linear-gradient(200deg, rgba(31,195,230,0.25) 0%, rgba(13,26,69,0) 70%);
  }
  .faint-hex-field {
    position: absolute;
    left: 0;
    top: 188px;
    width: 256px;
    height: 297px;
    background: radial-gradient(ellipse at 30% 70%, rgba(40,80,170,0.55) 0%, rgba(26,60,140,0.25) 55%, rgba(26,60,140,0) 85%);
  }

  .brand {
    position: absolute;
    left: 56px;
    top: 50px;
    display: flex;
    align-items: center;
    gap: 16px;
  }
  .brand__mark {
    width: 40px;
    height: 40px;
    border-radius: 50%;
    background: var(--brand-blue);
  }
  .brand__name {
    font-family: "Arimo", Arial, sans-serif;
    font-weight: 700;
    font-size: 30px;
    letter-spacing: 0.5px;
    color: var(--brand-blue);
    text-transform: uppercase;
  }

  .host-portrait {
    position: absolute;
    left: 207px;
    top: 116px;
    width: 429px;
    height: 369px;
    border-radius: 120px 120px 0 0;
    background: linear-gradient(180deg, var(--shirt-mid) 0%, var(--shirt-light) 60%, #d4e9f8 100%);
  }
</style>
</head>
<body>
<main class="sheet">
  <section class="backdrop backdrop--with-host" aria-label="Video call background with presenter">
    <div class="glow-hex-field" role="img" aria-label="Glowing cyan hexagon pattern"></div>
    <div class="faint-hex-field" role="img" aria-label="Faint blue hexagon pattern"></div>
    <div class="brand">
      <span class="brand__mark"></span>
      <span class="brand__name">Halvenrock Systems</span>
    </div>
    <div class="host-portrait" role="img" aria-label="Presenter portrait in light blue shirt"></div>
  </section>

  <section class="backdrop backdrop--plain" aria-label="Video call background">
    <div class="glow-hex-field" role="img" aria-label="Glowing cyan hexagon pattern"></div>
    <div class="faint-hex-field" role="img" aria-label="Faint blue hexagon pattern"></div>
    <div class="brand">
      <span class="brand__mark"></span>
      <span class="brand__name">Halvenrock Systems</span>
    </div>
  </section>
</main>
</body>
</html>
```